Verdant Loop Advisors, LLC

I am looking for a simple, clear layout with my logo prominent and embossed, on the best quality card stock available. I would like the business name and phone number included on the card as well......I dont want my name anywhere on the card and I would like my logo embossed on the card......something simple with a white back......open to designs as long as they go along with recycling symbols and green type stuff.....The address, website, cell number, fax number, and email are listed below

5374 Tillbury Fenwood Road
Brantmoor, MD 20912

c. 240.555.0143 f. 240.555.0187
e. sales@verdantloopadvisors.example
w. www.verdantloopadvisors.example

Industry/Entity Type

Recycling

```html
<!DOCTYPE html>
<html lang="en">
<head>
<meta charset="utf-8">
<title>Verdant Loop Advisors, LLC — Business Card</title>
<link rel="stylesheet" href="https://fonts.googleapis.com/css2?family=Open+Sans:wght@400;700&display=swap">
<style>
  :root {
    --backdrop: #ececec;
    --card: #ffffff;
    --ink: #1a1a1a;
    --green: #2f7d3a;
    --shadow: rgba(0, 0, 0, 0.18);
  }
  * { box-sizing: border-box; margin: 0; padding: 0; }
  html, body {
    width: 1200px;
    height: 800px;
    overflow: hidden;
    background: var(--backdrop);
    font-family: "Open Sans", Arial, sans-serif;
  }
  .card {
    position: absolute;
    left: 150px;
    top: 143px;
    width: 900px;
    height: 514px;
    background: var(--card);
    box-shadow: 0 10px 30px var(--shadow);
    color: var(--ink);
  }
  .brand {
    position: absolute;
    left: 70px;
    top: 70px;
    display: flex;
    align-items: center;
    gap: 20px;
  }
  .brand-mark {
    width: 66px;
    height: 66px;
    background: var(--green);
  }
  .brand-name {
    font-weight: 700;
    font-size: 38px;
    letter-spacing: 1px;
    color: var(--ink);
    text-transform: uppercase;
    line-height: 1;
  }
  .contact {
    position: absolute;
    left: 70px;
    font-size: 23px;
    line-height: 30px;
    list-style: none;
  }
  .contact li {
    display: flex;
    align-items: center;
    gap: 8px;
  }
  .contact svg {
    width: 20px;
    height: 20px;
    flex: none;
    fill: var(--green);
  }
  .contact .indent { padding-left: 28px; }
  .address { top: 255px; }
  .lines { top: 335px; }
</style>
</head>
<body>
  <main class="card">
    <div class="brand">
      <div class="brand-mark"></div>
      <div class="brand-name">Verdant Loop Advisors, LLC</div>
    </div>

    <ul class="contact address">
      <li>
        <svg viewBox="0 0 20 20" aria-hidden="true"><path d="M10 2 1 10h3v8h5v-5h2v5h5v-8h3z"/></svg>
        5374 Tillbury Fenwood Road
      </li>
      <li class="indent">Brantmoor, MD 20912</li>
    </ul>

    <ul class="contact lines">
      <li>
        <svg viewBox="0 0 20 20" aria-hidden="true"><path d="M6 1h8a1 1 0 0 1 1 1v16a1 1 0 0 1-1 1H6a1 1 0 0 1-1-1V2a1 1 0 0 1 1-1zm1 2v10h6V3zm3 12a1 1 0 1 0 0 2 1 1 0 0 0 0-2z"/></svg>
        240.555.0143
      </li>
      <li>
        <svg viewBox="0 0 20 20" aria-hidden="true"><path d="M5 2h8l2 2v4h2a1 1 0 0 1 1 1v7a1 1 0 0 1-1 1h-2v2H5v-2H3a1 1 0 0 1-1-1V9a1 1 0 0 1 1-1h2zm2 2v4h6V4zm0 9v4h6v-4z"/></svg>
        240.555.0187
      </li>
      <li>
        <svg viewBox="0 0 20 20" aria-hidden="true"><path d="M2 4h16a1 1 0 0 1 1 1v10a1 1 0 0 1-1 1H2a1 1 0 0 1-1-1V5a1 1 0 0 1 1-1zm0 2v.5l8 5 8-5V6l-8 5z"/></svg>
        sales@verdantloopadvisors.example
      </li>
      <li>
        <svg viewBox="0 0 20 20" aria-hidden="true"><path d="M10 1a9 9 0 1 0 0 18 9 9 0 0 0 0-18zm0 2c.9 0 2 1.6 2.5 4h-5C8 4.6 9.1 3 10 3zM7.3 9h5.4a14 14 0 0 1 0 2H7.3a14 14 0 0 1 0-2zM3.1 9h2.2a16 16 0 0 0 0 2H3.1a7 7 0 0 1 0-2zm11.6 0h2.2a7 7 0 0 1 0 2h-2.2a16 16 0 0 0 0-2zM7.5 13h5c-.5 2.4-1.6 4-2.5 4s-2-1.6-2.5-4z"/></svg>
        www.verdantloopadvisors.example
      </li>
    </ul>
  </main>
</body>
</html>
```